Business Card Design EFTPOS Comparison site

At QuoteHarbor.com.au we are a free service that allows our customers to get up to five quotes from our panel of suppliers for a range of BUSINESS related products and services. These products include eftpos / credit card machines, bank accounts, insurance, signage,office furniture etc. basically anything that a small business would need.
The process is done in 3 steps; 1) register your enquiry 2) we source and provide the five cheapest quotes 3) then select the supplier of your choice,the process is simple ABC and is FREE.
Please visit the soon to be revamped website to see our logo.
Target Market(s)
Small business operators
Industry/Entity Type
Small Business
Requirements
Must have
- Double Sided card

```html
<!DOCTYPE html>
<html lang="en">
<head>
<meta charset="utf-8">
<title>QuoteHarbor Business Card – Front and Back</title>
<link href="https://fonts.googleapis.com/css2?family=Crimson+Text:wght@400;600;700&display=swap" rel="stylesheet">
<style>
  :root {
    --stage: #e4e4e2;
    --card: #ffffff;
    --orange: #f39a1e;
    --orange-dark: #e0861a;
    --blue: #2f6fb3;
    --font-text: "Crimson Text", Georgia, serif;
  }
  * { margin: 0; padding: 0; box-sizing: border-box; }
  html, body {
    width: 1200px;
    height: 1200px;
    overflow: hidden;
    background: var(--stage);
    font-family: var(--font-text);
  }
  .canvas {
    position: relative;
    width: 1200px;
    height: 1200px;
  }
  .card {
    position: absolute;
    left: 160px;
    width: 880px;
    height: 500px;
    background: var(--card);
    box-shadow: 0 6px 18px rgba(0,0,0,0.18);
    overflow: hidden;
  }
  .card--front { top: 70px; }
  .card--back { top: 630px; }

  /* wordmark */
  .wordmark {
    position: absolute;
    display: flex;
    align-items: center;
    gap: 14px;
  }
  .wordmark__dot {
    border-radius: 50%;
    background: var(--blue);
    flex: none;
  }
  .wordmark__name {
    color: var(--orange);
    font-weight: 700;
    line-height: 1;
    white-space: nowrap;
  }
  .card--front .wordmark { left: 60px; top: 175px; }
  .card--front .wordmark__dot { width: 40px; height: 40px; }
  .card--front .wordmark__name { font-size: 52px; }

  .card--back .wordmark { left: 0; right: 0; top: 150px; justify-content: center; }
  .card--back .wordmark__dot { width: 64px; height: 64px; }
  .card--back .wordmark__name { font-size: 86px; }

  .site-url {
    position: absolute;
    color: var(--orange-dark);
    font-weight: 700;
    white-space: nowrap;
  }
  .card--front .site-url { left: 60px; top: 330px; font-size: 24px; }
  .card--back .site-url { left: 0; right: 0; top: 300px; text-align: center; font-size: 26px; }

  .divider {
    position: absolute;
    left: 470px;
    top: 40px;
    width: 3px;
    height: 300px;
    background: var(--orange);
  }

  .contact {
    position: absolute;
    left: 510px;
    top: 48px;
  }
  .contact__name {
    font-size: 40px;
    font-weight: 600;
    line-height: 1.1;
  }
  .contact__first { color: var(--orange); }
  .contact__last { color: var(--blue); }
  .contact__role {
    color: var(--orange);
    font-size: 20px;
    font-weight: 600;
    margin-top: 2px;
  }
  .contact__list {
    list-style: none;
    margin-top: 40px;
    font-size: 22px;
    line-height: 1.35;
  }
  .contact__list li:nth-child(3) { margin-top: 10px; }
  .contact__label { color: var(--blue); font-weight: 600; display: inline-block; width: 30px; }
  .contact__value { color: var(--orange-dark); font-weight: 600; }

  .service-band {
    position: absolute;
    left: 0;
    right: 0;
    top: 418px;
    height: 34px;
    padding: 0 40px;
    background: var(--orange);
    border-top: 4px solid var(--blue);
    color: #fff;
    font-size: 14px;
    letter-spacing: 1px;
    text-transform: uppercase;
    text-align: center;
    line-height: 30px;
    white-space: nowrap;
  }
  .card--back .service-band { font-size: 18px; letter-spacing: 1px; }
</style>
</head>
<body>
<main class="canvas">

  <section class="card card--front" aria-label="Business card front">
    <div class="wordmark">
      <span class="wordmark__dot"></span>
      <span class="wordmark__name">QuoteHarbor</span>
    </div>
    <p class="site-url">www.QuoteHarbor.com.au</p>
    <span class="divider"></span>
    <div class="contact">
      <h1 class="contact__name"><span class="contact__first">Daniel</span> <span class="contact__last">Reeves</span></h1>
      <p class="contact__role">Founder/Owner</p>
      <ul class="contact__list">
        <li><span class="contact__label">P:</span> <span class="contact__value">1300.555.014</span></li>
        <li><span class="contact__label">F:</span> <span class="contact__value">1300.555.015</span></li>
        <li><span class="contact__label">M:</span> <span class="contact__value">info@QuoteHarbor.com</span></li>
        <li><span class="contact__label">W:</span> <span class="contact__value">www.QuoteHarbor.com.au</span></li>
      </ul>
    </div>
    <p class="service-band">EFTPOS · Credit card machines · Bank accounts · Insurance · Signage · Office furniture</p>
  </section>

  <section class="card card--back" aria-label="Business card back">
    <div class="wordmark">
      <span class="wordmark__dot"></span>
      <span class="wordmark__name">QuoteHarbor</span>
    </div>
    <p class="site-url">www.QuoteHarbor.com.au</p>
    <p class="service-band">When we say “We guarantee to give you a better EFTPOS deal” we mean it!</p>
  </section>

</main>
</body>
</html>
```